Technology Enablement - One Pager

I need (2) one pager piece of marketing collateral to use as outreach for a service offering. The one pager must have a strong call to action, highlight the pain points the service solves.

```html
<!DOCTYPE html>
<html lang="en">
<head>
<meta charset="utf-8">
<title>Technology Enablement SMB – One Pager</title>
<link rel="stylesheet" href="https://fonts.googleapis.com/css2?family=Montserrat:wght@500;800&family=Poppins:wght@400;600;700;800&display=swap">
<style>
  :root{
    --navy:#0b1d55;
    --ink:#1b1b24;
    --brand-blue:#1273c4;
    --tick-blue:#1e8fe0;
    --magenta:#e21dc6;
    --pill-start:#8a1fb0;
    --pill-end:#3a1c9e;
    --panel-navy:#0c1f4e;
    --card-top:#7a22b0;
    --card-bottom:#2d4ba6;
    --cta-blue:#0877c2;
    --rule:#c9c9cf;
    --white:#ffffff;
  }
  *{box-sizing:border-box;margin:0;padding:0}
  html,body{width:1005px;height:1200px;overflow:hidden;background:var(--white)}
  body{font-family:"Poppins",sans-serif;color:var(--ink);position:relative}
  .abs{position:absolute}

  /* Title */
  .title{left:58px;top:40px;font-family:"Montserrat",sans-serif;color:var(--ink);line-height:1}
  .title .line1{font-size:45px;font-weight:500;letter-spacing:-1px}
  .title .line2{font-size:45px;font-weight:800;color:var(--navy);letter-spacing:-.5px;margin-top:-2px}
  .title .line3{font-size:88px;font-weight:800;color:var(--brand-blue);letter-spacing:-2px;margin-top:-6px}

  .rule{height:1px;background:var(--rule)}

  .headline{left:60px;top:236px;width:400px;font-size:21.5px;font-weight:700;line-height:26px;color:var(--ink)}
  .intro{left:61px;top:296px;width:380px;font-size:15px;line-height:18px;color:var(--ink)}

  .pill{height:29px;border-radius:15px;background:linear-gradient(90deg,var(--pill-start),var(--pill-end));
        color:var(--white);font-weight:700;font-size:16.5px;line-height:29px;padding-left:18px;letter-spacing:.1px}
  .pill-rule{height:1px;background:var(--rule)}

  p.body{font-size:12.2px;line-height:14.5px;color:var(--ink)}
  .sub{font-size:15px;font-weight:700;color:var(--navy);line-height:18px}

  ul.ticks{list-style:none}
  ul.ticks li{position:relative;padding-left:15px;font-size:12.2px;line-height:14px}
  ul.ticks li::before{content:"";position:absolute;left:0;top:3px;width:8px;height:8px;border-radius:50%;background:var(--tick-blue)}
  ul.ticks li::after{content:"";position:absolute;left:2.4px;top:4.6px;width:2.2px;height:3.4px;border:solid var(--white);border-width:0 1.2px 1.2px 0;transform:rotate(45deg)}
  ul.spaced li{margin-bottom:7.3px}
  ul.spaced li:last-child{margin-bottom:0}

  .slogan{left:60px;top:1083px;font-size:18px;font-weight:700;color:var(--magenta);line-height:18.5px}

  /* Right column */
  .illustration{left:530px;top:0;width:475px;height:345px;
    background:radial-gradient(ellipse at 55% 60%,#bfe3f5 0%,#dfe7fb 40%,#f4f6fc 70%,#ffffff 100%)}
  .navy-panel{left:503px;top:472px;width:502px;height:728px;background:var(--panel-navy);border-top-left-radius:22px}

  .product-card{left:542px;top:352px;width:400px;height:442px;border-radius:22px;color:var(--white);
    background:linear-gradient(30deg,var(--card-bottom) 0%,#4d38aa 45%,var(--card-top) 100%)}
  .product-card > *{position:absolute}
  .product-card .heading{left:38px;top:19px;font-size:18.5px;font-weight:700;line-height:22.5px}
  .product-card .heading span{color:var(--magenta)}
  .product-card .card-rule{left:38px;width:335px;height:1px;background:rgba(255,255,255,.35)}
  .product-card .engagement{left:38px;top:81px;font-size:15px;font-weight:700;line-height:18px}
  .product-card .label{left:38px;font-size:13px;font-weight:800;color:var(--magenta);line-height:16px}
  .product-card ul.assess{left:38px;top:124px}
  .product-card ul.assess li{font-size:12.3px;line-height:18.2px;padding-left:22px}
  .product-card ul.assess li::before{left:6px;top:5px}
  .product-card ul.assess li::after{left:8.4px;top:6.6px}
  .product-card .receive{left:38px;top:258px;font-size:13.5px;font-weight:700;line-height:16px}
  .product-card ul.factors{left:44px;top:303px;display:flex}
  .product-card ul.factors li{font-size:12.3px;line-height:15px;padding-left:13px}
  .product-card ul.factors li:nth-child(1){width:108px}
  .product-card ul.factors li:nth-child(2){width:90px}
  .product-card .price{left:38px;top:362px;font-weight:800;line-height:1}
  .price .word{font-size:30px;color:var(--magenta);letter-spacing:.5px}
  .price .amount{font-size:28px;margin-top:1px}
  .price .amount sup{font-size:14px;vertical-align:11px}
  .product-card .price-divider{left:156px;top:366px;width:1px;height:58px;background:rgba(255,255,255,.55)}
  .product-card .terms{left:172px;top:364px;width:200px;font-size:12.3px;line-height:14.5px}
  .terms b{font-weight:700}
  .terms p + p{margin-top:14px}

  .right-text{color:var(--white)}
  .right-text p.body{color:var(--white)}
  ul.right-list li{color:var(--white);padding-left:12px;line-height:15px;margin-bottom:3px}
  ul.right-list li:last-child{margin-bottom:0}
  .right-text .lead{font-size:12.2px;font-weight:600;color:var(--white);line-height:15px}

  .cta{left:542px;top:1097px;width:400px;height:103px;background:var(--cta-blue);border-radius:22px 22px 0 0;
       color:var(--white);padding:11px 0 0 26px;font-size:19px;font-weight:700;line-height:22px}
</style>
</head>
<body>

  <!-- Title block -->
  <div class="abs title">
    <div class="line1">TECHNOLOGY</div>
    <div class="line2">ENABLEMENT</div>
    <div class="line3">SMB</div>
  </div>
  <div class="abs rule" style="left:60px;top:222px;width:399px"></div>

  <h1 class="abs headline">Your technology shouldn’t slow<br>your business down.</h1>
  <p class="abs intro">We help SMBs turn disconnected tools into<br>systems that actually work.</p>

  <!-- The problem -->
  <div class="abs pill" style="left:60px;top:349px;width:208px">THE PROBLEM</div>
  <div class="abs pill-rule" style="left:268px;top:363px;width:191px"></div>
  <p class="abs body" style="left:60px;top:388px;width:360px">Most growing businesses have plenty of software<br>but no real system.</p>
  <p class="abs body" style="left:60px;top:425px;width:400px">You’ve invested in cloud tools, CRMs, accounting platforms,<br>HR apps, and automation. Yet day-to-day work still feels<br>harder than it should.</p>
  <h2 class="abs sub" style="left:60px;top:478px">Common pain points</h2>
  <ul class="abs ticks spaced" style="left:60px;top:502px">
    <li>Software doesn’t talk to each other</li>
    <li>Key processes live in people’s heads</li>
    <li>Manual work fills the gaps between systems</li>
    <li>Decisions are made without clear data</li>
    <li>Tech choices are made reactively, not strategically</li>
  </ul>
  <h2 class="abs sub" style="left:60px;top:613px">The result?</h2>
  <p class="abs body" style="left:60px;top:636px;width:340px">More effort, more admin, and less return on your<br>software spend.</p>

  <!-- What we do -->
  <div class="abs pill" style="left:60px;top:679px;width:208px">WHAT WE DO</div>
  <div class="abs pill-rule" style="left:268px;top:693px;width:191px"></div>
  <p class="abs body" style="left:60px;top:717px;width:400px"><b>Technology Enablement</b> is about improving how work<br>actually flows through your business</p>
  <h2 class="abs sub" style="left:60px;top:751px">Common pain points</h2>
  <ul class="abs ticks spaced" style="left:60px;top:775px">
    <li>Identify workflow and process gaps</li>
    <li>Find where technology is creating friction (not value)</li>
    <li>Improve adoption of the tools you already pay for</li>
    <li>Clarify where automation and integration will actually help</li>
    <li>Build a practical roadmap tied to real business outcomes</li>
  </ul>
  <h2 class="abs sub" style="left:60px;top:885px">This is not IT support</h2>
  <p class="abs body" style="left:60px;top:905px">It’s operational improvement, using technology as the lever.</p>

  <!-- Approach -->
  <div class="abs pill" style="left:60px;top:938px;width:322px;padding-left:16px">OUR APPROACH IS DIFFERENT</div>
  <div class="abs pill-rule" style="left:382px;top:952px;width:77px"></div>
  <ul class="abs ticks" style="left:60px;top:975px">
    <li style="padding-left:17px;line-height:15px">You <b>do not</b> need to switch IT providers</li>
    <li style="padding-left:17px;line-height:15px">You <b>do not</b> need to rip and replace systems</li>
    <li style="padding-left:17px;line-height:15px">You <b>do not</b> need a long-term contract</li>
  </ul>
  <p class="abs body" style="left:59px;top:1028px">We start with clarity first.<br>Execution comes later — only where it makes sense.</p>
  <div class="abs rule" style="left:60px;top:1070px;width:399px"></div>

  <div class="abs slogan">Start with insight.<br>Move forward with confidence.</div>
  <p class="abs body" style="left:60px;top:1122px;width:400px">Let’s identify what’s actually holding your business back —<br>and how to fix it.</p>

  <!-- Right column -->
  <div class="abs illustration" role="img" aria-label="Isometric illustration of a laptop, phone and data servers with small figures analysing dashboards, over a faint network of dots"></div>
  <div class="abs navy-panel"></div>

  <section class="abs product-card">
    <h2 class="heading"><span>PRODUCT 1:</span> TECHNOLOGY<br>ENABLEMENT ASSESSMENT</h2>
    <div class="card-rule" style="top:72px"></div>
    <div class="engagement">A 2–4 week, stand-alone engagement</div>
    <div class="label" style="top:109px">We assess your</div>
    <ul class="ticks assess">
      <li>Technology &amp; digital maturity</li>
      <li>Core workflows and handoffs</li>
      <li>Integration and automation opportunities</li>
      <li>Adoption gaps and training needs</li>
      <li>Data, reporting, and KPI visibility</li>
      <li>IT and security posture (at a business level)</li>
    </ul>
    <div class="label" style="top:241px">You receive</div>
    <div class="receive">A prioritized 5–10 item Improvement<br>Roadmap, each with</div>
    <ul class="ticks factors">
      <li>Business<br>impact</li>
      <li>Relative<br>effort</li>
      <li>ROI<br>potential</li>
    </ul>
    <div class="card-rule" style="top:349px"></div>
    <div class="price">
      <div class="word">PRICE</div>
      <div class="amount"><sup>$</sup>2,500</div>
    </div>
    <div class="price-divider"></div>
    <div class="terms">
      <p><b>No</b> upsell required.</p>
      <p><b>No</b> obligation beyond the assessment.</p>
    </div>
  </section>

  <div class="abs pill" style="left:552px;top:813px;width:212px;padding-left:18px">WHO THIS IS FOR</div>
  <ul class="abs ticks right-list" style="left:555px;top:848px">
    <li>Small and mid-sized businesses</li>
    <li>Leadership teams feeling “tech pressure”<br>but lacking a plan</li>
    <li>Companies scaling headcount faster than systems</li>
    <li>Owners tired of guessing which tools to buy next</li>
  </ul>

  <div class="abs pill" style="left:552px;top:943px;width:212px;padding-left:18px">WHY START HERE</div>
  <div class="abs right-text" style="left:555px;top:977px;width:380px">
    <p class="body">Because buying more software without fixing workflows<br>just adds complexity</p>
    <p class="lead" style="margin-top:7px">This assessment gives you</p>
  </div>
  <ul class="abs ticks right-list" style="left:555px;top:1031px">
    <li>Clarity instead of opinions</li>
    <li>A roadmap instead of random fixes</li>
    <li>Confidence before spending more money</li>
  </ul>

  <div class="abs cta">Book a Technology Enablement<br>Assessment</div>

</body>
</html>
```